Can Design for Fun, Growing Health Food Brand

We are launching a brand new product, electrolyte seltzer drinks. We want the design to be clean/simple and slightly modern while staying true to our brand identity. Must say "Mineral Hydration" as the product descriptor, sub headline is "Carbonated electrolyte beverage with sea moss and real fruit juice". First flavors will be Watermelon Mint and Mango.

Target Market(s)

Women ages 30-50 who are interested in health wellness/trends

Industry/Entity Type

Health & Wellness

Font styles to use
Sans Serif

Requirements
Must have
• Tall, skinny can, current Brightfen Kelp Logo, use aluminum on can as element in design.
Nice to have
• Be fun, clean and modern. Would like to see the label less busy than our gels.
Should not have
• Avoid putting flavor on bottom 1/5 of can. No gradient color changes. Do not want really detailed or realistic fruit image, prefer drawings or similar.

```html
<!DOCTYPE html>
<html lang="en">
<head>
<meta charset="utf-8">
<title>Brightfen Kelp – Mineral Hydration Can Labels</title>
<link rel="stylesheet" href="https://fonts.googleapis.com/css2?family=Montserrat:wght@700;900&family=Oswald:wght@400;500&display=swap">
<style>
  :root {
    --paper: #ffffff;
    --frame: #9a9a9a;
    --brand-teal: #3f6e6c;
    --type-white: #ffffff;
    --mango-band: #ffcc00;
    --melon-band: #006837;
  }
  html, body {
    margin: 0;
    padding: 0;
    width: 685px;
    height: 1200px;
    overflow: hidden;
    background: var(--paper);
  }
  .sheet {
    width: 685px;
    height: 1200px;
    display: flex;
    justify-content: center;
    align-items: center;
    gap: 15px;
  }
  .label {
    width: 320px;
    height: 512px;
    border: 1px solid var(--frame);
    display: block;
    background: var(--paper);
  }
  .label--mango { --band: var(--mango-band); }
  .label--melon { --band: var(--melon-band); }
  .band-area { fill: var(--band); }
  .brand-dot { fill: none; stroke: var(--brand-teal); stroke-width: 3; }
  .brand-name {
    fill: var(--brand-teal);
    font-family: "Oswald", sans-serif;
    font-weight: 400;
    font-size: 40px;
  }
  .flavor {
    fill: var(--type-white);
    font-family: "Montserrat", sans-serif;
    font-weight: 700;
    font-size: 27px;
  }
  .descriptor {
    fill: var(--type-white);
    font-family: "Montserrat", sans-serif;
    font-weight: 900;
    font-size: 104px;
  }
  .subheadline {
    fill: var(--type-white);
    font-family: "Oswald", sans-serif;
    font-weight: 500;
    font-size: 29px;
  }
</style>
</head>
<body>
<main class="sheet">

  <svg class="label label--mango" viewBox="0 0 641 1025" aria-label="Mango can label">
    <rect class="band-area" x="0" y="185" width="641" height="840" role="img" aria-label="Yellow folded ribbon graphic"/>
    <circle class="brand-dot" cx="322" cy="68" r="22"/>
    <text class="brand-name" x="322" y="142" text-anchor="middle">Brightfen Kelp</text>
    <text class="flavor" x="307" y="322" text-anchor="end">MANGO</text>
    <text class="descriptor" transform="translate(307 985) rotate(-90)" textLength="560" lengthAdjust="spacingAndGlyphs">MINERAL</text>
    <text class="descriptor" transform="translate(397 985) rotate(-90)" textLength="680" lengthAdjust="spacingAndGlyphs">HYDRATION</text>
    <text class="subheadline" transform="translate(440 985) rotate(-90)" textLength="680" lengthAdjust="spacingAndGlyphs">CARBONATED ELECTROLYTE BEVERAGE WITH SEA MOSS AND REAL FRUIT JUICE</text>
  </svg>

  <svg class="label label--melon" viewBox="0 0 641 1025" aria-label="Watermelon Mint can label">
    <rect class="band-area" x="0" y="185" width="641" height="840" role="img" aria-label="Green folded ribbon graphic"/>
    <circle class="brand-dot" cx="322" cy="68" r="22"/>
    <text class="brand-name" x="322" y="142" text-anchor="middle">Brightfen Kelp</text>
    <text class="flavor" x="307" y="320" text-anchor="end">WATERMELON</text>
    <text class="flavor" x="307" y="347" text-anchor="end">MINT</text>
    <text class="descriptor" transform="translate(307 985) rotate(-90)" textLength="560" lengthAdjust="spacingAndGlyphs">MINERAL</text>
    <text class="descriptor" transform="translate(397 985) rotate(-90)" textLength="680" lengthAdjust="spacingAndGlyphs">HYDRATION</text>
    <text class="subheadline" transform="translate(440 985) rotate(-90)" textLength="680" lengthAdjust="spacingAndGlyphs">CARBONATED ELECTROLYTE BEVERAGE WITH SEA MOSS AND REAL FRUIT JUICE</text>
  </svg>

</main>
</body>
</html>
```